Business Card Design Project

We need a business card design for a new company focused on educational technology called 'Bright Harbor Educational Consulting'. We are a consulting company that helps other technology companies and schools market their solutions.

The final design should communicate the positive future of education, which is digital.

Industry/Entity Type

Business

Requirements
Nice to have
• four color, front and back.

```html
<!DOCTYPE html>
<html lang="en">
<head>
<meta charset="utf-8">
<title>Bright Harbor Educational Consulting – Business Cards</title>
<link rel="stylesheet" href="https://fonts.googleapis.com/css2?family=Open+Sans:wght@400;600&display=swap">
<style>
  :root {
    --stage: #2b2b2b;
    --paper: #ffffff;
    --ink: #1a1d3a;
    --navy: #1b2260;
    --lime: #8fd21b;
    --lime-deep: #5aae10;
    --orange: #f39420;
    --sky-light: #4cc3ff;
    --sky: #0a8ee0;
    --sky-deep: #03306a;
    --white: #ffffff;
  }
  * { margin: 0; padding: 0; box-sizing: border-box; }
  html, body { width: 1200px; height: 927px; overflow: hidden; }
  body {
    background: var(--stage);
    font-family: "Open Sans", Arial, sans-serif;
    position: relative;
  }
  .card {
    position: absolute;
    left: 250px;
    width: 700px;
    height: 400px;
    overflow: hidden;
    box-shadow: 0 12px 30px rgba(0,0,0,.5);
  }
  /* Front: contact side */
  .card-front { top: 48px; background: var(--paper); }
  .footer-band {
    position: absolute;
    left: 0; right: 0; bottom: 0;
    height: 90px;
    background: linear-gradient(180deg, var(--paper) 0%, var(--lime) 30%, var(--lime-deep) 100%);
  }
  .brand {
    position: absolute;
    display: flex;
    align-items: center;
    gap: 12px;
    color: var(--navy);
    font-weight: 600;
    text-transform: uppercase;
    line-height: 1;
  }
  .brand-mark { width: 22px; height: 22px; background: var(--navy); flex: none; }
  .card-front .brand { left: 320px; top: 70px; font-size: 22px; }
  .brand small { display: block; font-size: .45em; letter-spacing: .32em; margin-top: 6px; font-weight: 600; }
  .contact {
    position: absolute;
    left: 60px;
    top: 168px;
    font-size: 16px;
    line-height: 22px;
    color: var(--ink);
    list-style: none;
  }
  .holder {
    position: absolute;
    left: 420px;
    top: 168px;
    font-size: 16px;
    line-height: 22px;
    color: var(--ink);
  }
  /* Back: brand side */
  .card-back {
    top: 478px;
    background:
      radial-gradient(ellipse 55% 70% at 45% 50%, var(--sky-light) 0%, var(--sky) 55%, transparent 100%),
      linear-gradient(135deg, var(--sky) 0%, var(--sky-deep) 100%);
  }
  .card-back .brand {
    left: 50%; top: 150px;
    transform: translateX(-50%);
    font-size: 34px;
    white-space: nowrap;
  }
  .website {
    position: absolute;
    left: 0; right: 0;
    top: 262px;
    text-align: center;
    color: var(--white);
    font-size: 15px;
    letter-spacing: .3em;
  }
</style>
</head>
<body>
  <section class="card card-front" aria-label="Card front">
    <div class="footer-band" role="img" aria-label="Decorative green wave with an orange accent stripe along the bottom of the card"></div>
    <div class="brand">
      <span class="brand-mark"></span>
      <span>Bright Harbor<small>Educational Consulting</small></span>
    </div>
    <ul class="contact">
      <li>P.O. Box 0000</li>
      <li>your city,0000</li>
      <li>Tel: 0000000</li>
      <li>Fax: 0000000</li>
      <li>Email: mail@brightharbor.com</li>
    </ul>
    <div class="holder">
      <p>Name goes here</p>
      <p>Title</p>
    </div>
  </section>

  <section class="card card-back" aria-label="Card back">
    <div class="brand">
      <span class="brand-mark"></span>
      <span>Bright Harbor<small>Educational Consulting</small></span>
    </div>
    <p class="website">www.brightharbor.com</p>
  </section>
</body>
</html>
```